Free offer card

I need a business card sized FREE CLASS offer thing....Our target market is 18-40 year old women. We are the "sexy" pole studio but don't want to scare people off. This card will be given out by students and staff when they meet people that are interested and also put in hair dressers and sports shops etc. I've got HEAPS of photos so I'll upload a few, I'll also upload the last brochure we did but I'm not sure it's really doing it's job....might be a little scary? The free trial class maybe wasn't clear enough. I think maybe free class instead of using the word "trial" so they don't think they are going to get a hard sell. Need a space we can write student/teachers name on it...maybe Marla's Muse_________
And need both studios details on it (on attached brochure) happy to send different photos if it helps
I can get high res stuff and better copies of the fit fierce sexy brochure if you want...haven't used this website before not really sure what you need

```html
<!DOCTYPE html>
<html lang="en">
<head>
<meta charset="utf-8">
<title>Free Class Offer Card</title>
<link href="https://fonts.googleapis.com/css2?family=Lobster&family=Ropa+Sans&display=swap" rel="stylesheet">
<style>
  :root{
    --page:#ffffff;
    --card-dark:#1d1d1f;
    --card-mid:#3a3a3d;
    --pink:#e4008a;
    --white:#ffffff;
    --field:#f7f7f7;
    --field-border:#1e1e1e;
    --label:#555555;
    --glow:#5a4fd6;
  }
  *{margin:0;padding:0;box-sizing:border-box;}
  html,body{width:1200px;height:875px;overflow:hidden;background:var(--page);}
  .offer-card{
    position:absolute;left:60px;top:79px;width:1080px;height:717px;overflow:hidden;
    background:
      radial-gradient(ellipse 520px 300px at 520px 120px, var(--card-mid), transparent 75%),
      linear-gradient(180deg, #2c2c2e, var(--card-dark));
    font-family:"Ropa Sans", sans-serif;color:var(--white);
  }
  .studio-name{
    position:absolute;left:46px;top:56px;width:460px;
    font-size:50px;line-height:56px;color:var(--white);text-transform:uppercase;white-space:nowrap;
  }
  .studio-url{
    position:absolute;left:48px;top:176px;font-size:18px;letter-spacing:4.6px;color:var(--white);white-space:nowrap;
  }
  .offer-band{position:absolute;left:0;top:256px;width:1080px;height:242px;background:var(--pink);}
  .offer-title{
    position:absolute;left:52px;top:261px;font-family:"Lobster", cursive;font-size:138px;font-weight:400;
    line-height:150px;color:var(--white);white-space:nowrap;
  }
  .name-field{
    position:absolute;left:60px;top:416px;width:554px;height:70px;background:var(--field);
    border:2px solid var(--field-border);border-radius:10px;
  }
  .name-field-label{position:absolute;left:8px;bottom:4px;font-size:14px;color:var(--label);}
  .dancer-photo{
    position:absolute;left:680px;top:0;width:300px;height:660px;
    background:linear-gradient(180deg, rgba(160,110,80,.35) 0%, rgba(150,95,70,.55) 45%, rgba(60,35,30,.6) 100%);
  }
  .floor-glow{
    position:absolute;left:660px;top:548px;width:440px;height:140px;border-radius:50%;
    background:radial-gradient(ellipse at center, rgba(90,79,214,.75), rgba(90,79,214,.25) 55%, transparent 72%);
  }
  .studio-address{position:absolute;top:541px;font-size:26px;line-height:35px;font-style:normal;white-space:nowrap;}
  .studio-address h2{font-weight:400;font-size:26px;line-height:35px;text-transform:uppercase;}
  .studio-address.northgate{left:38px;}
  .studio-address.wattle-bay{left:365px;}
</style>
</head>
<body>
  <div class="offer-card">
    <div class="floor-glow"></div>
    <div class="dancer-photo" role="img" aria-label="Photo of a pole dancer in black heels holding an inverted pose on a brass pole"></div>

    <div class="studio-name">Marla's Muse<br>Pole Studio</div>
    <div class="studio-url">www.marlasmusestudio.com.au</div>

    <div class="offer-band"></div>
    <h1 class="offer-title">Free Class</h1>
    <div class="name-field"><span class="name-field-label">student/teacher</span></div>

    <address class="studio-address northgate">
      <h2>Northgate Studio</h2>
      Level 2, 48 Harbour Lane,<br>
      Northgate NSW 2710<br>
      (02) 5550-0147
    </address>
    <address class="studio-address wattle-bay">
      <h2>Wattle Bay Studio</h2>
      4/62 Bayview Pde,<br>
      Wattle Bay NSW 2845<br>
      (02) 5550-2281
    </address>
  </div>
</body>
</html>
```